Artisan Bread Company needs a business card

I need a business card design, for an artisan bread company called "Holloway's Bread".

I would like the logo on one side, and on the other, I would like it to say

Dorian Holloway
Baker
416.552.0193
hollowaysbread@breadmail.example

Not necessarily in that order- but it must have these.

Industry/Entity Type

Business

Font styles to use
Serif

Requirements
Must have
• The provided logo on the front, this on the back-
• Dorian Holloway
• Baker
• 416.552.0193
• hollowaysbread@breadmail.example

```html
<!DOCTYPE html>
<html lang="en">
<head>
<meta charset="utf-8">
<title>Holloway's Bread — Business Card</title>
<link href="https://fonts.googleapis.com/css2?family=Montserrat:wght@400;600&display=swap" rel="stylesheet">
<style>
  :root {
    --page-bg: #e9e6e1;
    --card-bg: #2a2a2a;
    --card-shadow: rgba(0, 0, 0, 0.28);
    --ink-light: #f4f4f4;
    --ink-soft: #d8d8d8;
    --rule: #e6e6e6;
  }
  * { box-sizing: border-box; margin: 0; padding: 0; }
  html, body {
    width: 1200px;
    height: 800px;
    overflow: hidden;
  }
  body {
    background: var(--page-bg);
    font-family: "Montserrat", sans-serif;
    display: flex;
    flex-direction: column;
    align-items: center;
    justify-content: center;
    gap: 44px;
  }
  .card {
    position: relative;
    width: 600px;
    height: 330px;
    background: var(--card-bg);
    border-radius: 16px;
    box-shadow: 0 6px 18px var(--card-shadow);
    color: var(--ink-light);
  }
  .card-front .identity {
    position: absolute;
    left: 54px;
    top: 84px;
  }
  .card-front .person-name {
    font-weight: 600;
    font-size: 21px;
    letter-spacing: 0.02em;
    text-transform: uppercase;
  }
  .card-front .person-role {
    font-weight: 400;
    font-size: 15px;
    color: var(--ink-soft);
    margin-top: 4px;
  }
  .card-front .contact {
    position: absolute;
    left: 62px;
    bottom: 52px;
    font-size: 14.5px;
    line-height: 1.35;
    color: var(--ink-soft);
    list-style: none;
  }
  .card-back {
    display: flex;
    align-items: center;
    justify-content: center;
  }
  .brand-lockup {
    display: flex;
    flex-direction: column;
    align-items: center;
    gap: 10px;
  }
  .brand-name {
    font-weight: 400;
    font-size: 40px;
    letter-spacing: 0.02em;
    color: var(--ink-light);
  }
  .brand-rule {
    width: 260px;
    height: 1px;
    background: var(--rule);
  }
</style>
</head>
<body>
  <section class="card card-front" aria-label="Business card, contact side">
    <div class="identity">
      <h1 class="person-name">Dorian Holloway</h1>
      <p class="person-role">Baker</p>
    </div>
    <ul class="contact">
      <li class="contact-phone">416.552.0193</li>
      <li class="contact-email">hollowaysbread@breadmail.example</li>
    </ul>
  </section>

  <section class="card card-back" aria-label="Business card, brand side">
    <div class="brand-lockup">
      <p class="brand-name">Holloway's Bread</p>
      <span class="brand-rule"></span>
    </div>
  </section>
</body>
</html>
```